Webpage for a treatment housing for young addicts.

I need a new design and files for my wordpress page. I need it to be more neat and clean. I need it to look professional with a starting page that will work as a navigation. I need like logo and phone number and such up top, a picture under it with one sentence as a slogan and under it 6 boxes to click to come to our different pages. Under it I want news etc.

Target Market(s)

Social services, employees and governements

Coding

Coded - Design and coding required

Font styles to use
Sans Serif

Colors
abd037
3176b5
9d9d9d
aaaaaa
f04a50

Requirements
Must have
• A nice design
Nice to have
• need it to look professional with a starting page that will work as a navigation. I need like logo and phone number and such up top, a picture under it with one sentence as a slogan and under it 6 boxes to click to come to our different pages. Under it I want news etc.
• today www.kolrev.se
• want more like www.tralvik.se or www.bersona.se
Should not have
• To many different colours and a messy design.

```html
<!DOCTYPE html>
<html lang="en">
<head>
<meta charset="utf-8">
<title>Kolrev AB – Omsorg Vård Boende</title>
<link rel="stylesheet" href="https://fonts.googleapis.com/css2?family=Montserrat:ital,wght@0,400;0,500;0,600;0,700;0,800;1,400&display=swap">
<style>
:root{
  --green:#abd037;
  --green-dark:#8cb83a;
  --blue:#3176b5;
  --navy:#2f4a8f;
  --ink:#1d1d1f;
  --grey:#9d9d9d;
  --grey-light:#aaaaaa;
  --panel:#e6e5e3;
  --footer:#1b1c21;
  --footer-bar:#131418;
  --red:#f04a50;
}
*{box-sizing:border-box;margin:0;padding:0}
html,body{width:1200px;height:2410px;overflow:hidden}
body{font-family:"Montserrat",sans-serif;color:var(--ink);background:#fff;position:relative}
a{color:inherit;text-decoration:none}

/* header */
.site-header{position:absolute;left:0;top:0;width:1200px;height:112px;background:#fff}
.brand{position:absolute;left:22px;top:22px;display:flex;align-items:center;gap:10px}
.brand-dot{width:26px;height:26px;border-radius:50%;background:var(--green)}
.brand-name{font-size:40px;font-weight:800;color:var(--blue);letter-spacing:-1px;line-height:1}
.brand-tag{position:absolute;left:58px;top:70px;font-size:10px;letter-spacing:1.5px;color:#666}
.news-ticker{position:absolute;left:297px;top:0;width:762px;height:39px;background:var(--green);display:flex;align-items:center;font-size:12px}
.news-ticker .label{font-weight:700;font-size:15px;padding:0 12px 0 16px;border-right:2px solid var(--ink);line-height:18px;white-space:nowrap}
.news-ticker .text{padding-left:18px;font-weight:600;flex:1;white-space:nowrap}
.news-ticker .treat{font-weight:700;letter-spacing:1px;padding-right:16px;display:flex;align-items:center;gap:6px}
.contact-tab{position:absolute;left:1059px;top:0;width:141px;height:39px;background:var(--navy);color:#fff;font-size:13px;font-weight:700;letter-spacing:1.5px;display:flex;align-items:center;justify-content:center;gap:8px}
.header-info{position:absolute;top:39px;height:73px;display:flex;align-items:center;border-left:1px solid #ccc}
.phone-block{left:610px;border:none;gap:14px;font-size:17px;font-weight:600;letter-spacing:1.5px;color:#555}
.hours-block{left:805px;width:217px;padding-left:16px;gap:12px;font-size:13px;font-weight:700;letter-spacing:1px;color:#555;line-height:21px}
.search-block{left:1022px;width:90px;justify-content:center}
.menu-block{left:1112px;width:88px;justify-content:center}

/* hero */
.hero{position:absolute;left:0;top:112px;width:1200px;height:463px;background:linear-gradient(100deg,#4c4a44 0%,#6e6c66 25%,#b9bfc4 48%,#dfe2e3 68%,#c9ccce 85%,#8b8e90 100%)}
.hero-title{position:absolute;left:632px;top:100px;width:540px;font-size:43px;font-weight:700;line-height:49px;letter-spacing:1px}
.hero-title em{font-style:normal;color:var(--green-dark)}
.btn{display:flex;align-items:center;justify-content:center;background:var(--blue);color:#fff;font-weight:700;border-radius:24px;position:absolute;letter-spacing:1px}
.hero .btn{left:635px;top:280px;width:171px;height:44px;font-size:16px;letter-spacing:1.5px}

/* nav tiles */
.tiles{position:absolute;left:0;top:575px;width:1200px;height:268px;background:var(--panel)}
.tile{position:absolute;width:258px;height:65px;background:#fff;border:1px solid var(--navy);display:flex;align-items:center;justify-content:space-between;padding:0 22px 0 28px;font-size:16px;font-weight:700;letter-spacing:1px;white-space:nowrap}
.tile .arrow{flex:none;width:32px;height:32px;border-radius:50%;background:var(--navy);display:flex;align-items:center;justify-content:center}
.tile.active{background:var(--navy);color:#fff}
.tile.active .arrow{background:#fff}

/* headings */
.section-title{position:absolute;font-size:36px;font-weight:700;letter-spacing:1px}
.section-title::after{content:"";position:absolute;left:2px;top:52px;width:38px;height:4px;background:var(--green)}

/* news */
.news{position:absolute;left:0;top:843px;width:1200px;height:568px;background:#fff}
.card{position:absolute;top:165px;width:272px}
.card .media{width:270px;height:168px}
.card h3{margin-top:16px;font-size:15px;font-weight:700;color:var(--navy);letter-spacing:.8px;text-decoration:underline;text-underline-offset:4px}
.card .date{margin-top:12px;font-size:12px;color:var(--grey);font-weight:500}
.card p{margin-top:12px;font-size:14px;color:#666;line-height:17px}
.play{position:absolute;left:119px;top:68px;width:34px;height:34px;border-radius:50%;background:rgba(255,255,255,.9)}
.news .btn{left:535px;top:486px;width:130px;height:33px;font-size:15px}

/* about */
.about{position:absolute;left:0;top:1411px;width:1200px;height:417px;background:var(--green)}
.about .section-title{color:var(--ink)}
.about .section-title::after{background:var(--ink);width:62px}
.about-text{position:absolute;left:189px;top:158px;width:545px;font-size:13.5px;line-height:21px;letter-spacing:.3px;color:#2b2b2b}
.about-text b{font-weight:700}
.about .btn{left:183px;top:330px;width:129px;height:34px;font-size:15px}
.about-media{position:absolute;left:757px;top:160px;width:270px;height:201px;background:linear-gradient(135deg,#cfd6de,#9ba6b3 55%,#c9a9b4)}

/* footer */
.site-footer{position:absolute;left:0;top:1828px;width:1200px;height:540px;background:var(--footer);color:#fff}
.footer-brand{position:absolute;left:187px;top:60px;display:flex;align-items:center;gap:10px}
.footer-brand .brand-dot{background:#4a4b50}
.footer-brand .brand-name{color:#4a4b50}
.footer-col{position:absolute;top:170px;width:270px}
.footer-col h4{font-size:20px;font-weight:700;letter-spacing:1px;position:relative}
.footer-col h4::after{content:"";position:absolute;left:0;top:34px;width:39px;height:3px;background:#fff}
.contact-list{margin-top:28px;list-style:none}
.contact-list li{display:flex;gap:14px;font-size:13px;font-weight:700;letter-spacing:.8px;color:#bfc0c4;line-height:24px;margin-bottom:10px}
.contact-list span{width:240px}
.contact-list svg{flex:none;margin-top:3px}
.org{font-size:15px;font-weight:700;color:var(--green);letter-spacing:1px;margin-top:10px}
.site-footer .btn{position:static;margin-top:32px;width:165px;height:36px;font-size:14px}
.links{margin-top:28px;list-style:none}
.links li{font-size:14px;color:#55565b;letter-spacing:1px;line-height:27.5px}
.newsletter p{margin-top:38px;font-size:14px;color:#9a9ba0;letter-spacing:1px;line-height:19px}
.signup{margin-top:22px;width:270px;height:38px;border:1px solid #9a9ba0;border-radius:3px;display:flex;align-items:center;justify-content:space-between;padding:0 3px 0 16px}
.signup span{font-size:14px;font-style:italic;color:#9a9ba0}
.signup b{background:var(--blue);border-radius:3px;font-size:12px;padding:6px 12px}
.socials{display:flex;gap:12px;margin-top:44px}
.social{position:relative;width:72px;height:72px;border-radius:50%;border:2px solid #fff}
.social i{position:absolute;right:4px;bottom:-8px;width:28px;height:28px;border-radius:50%;border:2px solid #fff}
.copyright{position:absolute;left:0;top:2368px;width:1200px;height:42px;background:var(--footer-bar);color:#fff;font-size:12px;display:flex;align-items:center;justify-content:center;letter-spacing:.5px}
</style>
</head>
<body>

<header class="site-header">
  <div class="brand"><span class="brand-dot"></span><span class="brand-name">Kolrev AB</span></div>
  <div class="brand-tag">Omsorg Vård Boende</div>
  <div class="news-ticker">
    <span class="label">Latest News</span>
    <span class="text">Ut enim ad minima veniam, quis nostrum ....</span>
    <span class="treat"><svg width="20" height="14" viewBox="0 0 20 14"><path d="M1 2 Q10 0 19 4 Q12 6 9 13 Q6 6 1 2Z" fill="#1d1d1f"/></svg>TREATMENT</span>
  </div>
  <div class="contact-tab"><svg width="15" height="15" viewBox="0 0 16 16"><path d="M15 1 L1 7 L7 9 L9 15 Z" fill="none" stroke="#fff" stroke-width="1.3"/></svg>CONTACT</div>
  <div class="header-info phone-block">
    <svg width="34" height="34" viewBox="0 0 34 34"><path d="M8 4 L13 10 L10 14 Q13 21 20 24 L24 21 L30 26 L26 31 Q12 30 3 10 Z" fill="none" stroke="#888" stroke-width="1.6"/><path d="M20 7 Q26 8 27 14 M20 2 Q31 3 32 14" fill="none" stroke="#888" stroke-width="1.6"/></svg>
    010-4407215
  </div>
  <div class="header-info hours-block">
    <svg width="40" height="40" viewBox="0 0 40 40"><circle cx="20" cy="20" r="18" fill="none" stroke="#777" stroke-width="2.5"/><path d="M20 9 V21 H29" fill="none" stroke="#777" stroke-width="2.5"/></svg>
    <span>Monday to Friday<br>9AM - 6PM</span>
  </div>
  <div class="header-info search-block"><svg width="44" height="44" viewBox="0 0 44 44"><circle cx="18" cy="18" r="14" fill="none" stroke="#666" stroke-width="2.5"/><path d="M28 28 L41 41" stroke="#666" stroke-width="3"/></svg></div>
  <div class="header-info menu-block"><svg width="42" height="36" viewBox="0 0 42 36"><path d="M0 4 H42 M0 18 H42 M0 32 H42" stroke="#666" stroke-width="4"/></svg></div>
</header>

<section class="hero" role="img" aria-label="Hiker with a backpack sitting on a rocky cliff edge above snowy mountains under a cloudy sky">
  <h1 class="hero-title">We create <em>sustainable pathways</em> to a better future</h1>
  <a class="btn" href="#">LEARN MORE</a>
</section>

<nav class="tiles">
  <a class="tile active" style="left:183px;top:59px" href="#">Quality Work<span class="arrow"><svg width="12" height="14" viewBox="0 0 12 14"><path d="M3 1 L9 7 L3 13" fill="none" stroke="#2f4a8f" stroke-width="2"/></svg></span></a>
  <a class="tile" style="left:471px;top:59px" href="#">Treatment<span class="arrow"><svg width="12" height="14" viewBox="0 0 12 14"><path d="M3 1 L9 7 L3 13" fill="none" stroke="#fff" stroke-width="2"/></svg></span></a>
  <a class="tile" style="left:764px;top:59px" href="#">Values Base<span class="arrow"><svg width="12" height="14" viewBox="0 0 12 14"><path d="M3 1 L9 7 L3 13" fill="none" stroke="#fff" stroke-width="2"/></svg></span></a>
  <a class="tile" style="left:183px;top:147px" href="#">Ethical Approach<span class="arrow"><svg width="12" height="14" viewBox="0 0 12 14"><path d="M3 1 L9 7 L3 13" fill="none" stroke="#fff" stroke-width="2"/></svg></span></a>
  <a class="tile" style="left:471px;top:147px" href="#">Team<span class="arrow"><svg width="12" height="14" viewBox="0 0 12 14"><path d="M3 1 L9 7 L3 13" fill="none" stroke="#fff" stroke-width="2"/></svg></span></a>
  <a class="tile" style="left:764px;top:147px" href="#">Career<span class="arrow"><svg width="12" height="14" viewBox="0 0 12 14"><path d="M3 1 L9 7 L3 13" fill="none" stroke="#fff" stroke-width="2"/></svg></span></a>
</nav>

<section class="news">
  <h2 class="section-title" style="left:185px;top:50px">NEWS</h2>
  <article class="card" style="left:172px">
    <div class="media" role="img" aria-label="Man in a life vest fishing beside blue water" style="background:linear-gradient(120deg,#2f6fa6,#1d4f80 60%,#6b5a4c)"></div>
    <h3>Lorem ipsum dolor sit amet</h3>
    <div class="date">December 1, 2018</div>
    <p>Sed ut perspiciatis unde omnis iste natus error[...]</p>
  </article>
  <article class="card" style="left:464px">
    <div class="media" role="img" aria-label="Two young people in helmets at an indoor go-kart track" style="background:linear-gradient(120deg,#3a3a3c,#6e6a64 50%,#2b2b2d)"></div>
    <h3>Lorem ipsum dolor sit amet</h3>
    <div class="date">December 1, 2018</div>
    <p>Sed ut perspiciatis unde omnis iste natus error[...]</p>
  </article>
  <article class="card" style="left:756px">
    <div class="media" role="img" aria-label="Group in life vests in a small boat among lily pads, video" style="position:relative;background:linear-gradient(120deg,#4f6e3a,#2e4d6e 50%,#5e8a3f)">
      <span class="play"><svg width="34" height="34" viewBox="0 0 34 34"><path d="M13 10 L24 17 L13 24Z" fill="#2f4a8f"/></svg></span>
    </div>
    <h3>Lorem ipsum dolor sit amet</h3>
    <div class="date">December 1, 2018</div>
    <p>Sed ut perspiciatis unde omnis iste natus error[...]</p>
  </article>
  <a class="btn" href="#">View All</a>
</section>

<section class="about">
  <h2 class="section-title" style="left:183px;top:50px">ABOUT US</h2>
  <p class="about-text"><b>Kolrev Sverige AB</b> carries out care and care for persons aged <b>14-25 years</b>. This is mainly done through <b>Home for Care and Housing (HVB)</b> . We are specialists in psychosocial abuse and crime problems. By constantly being open to new methods and well aware of the existing ones that work, we develop and improve the care. The methods are adapted to the individual, we do not believe that <b>ONE thought or ONE</b> perspective can be applied to everyone.</p>
  <a class="btn" href="#">More</a>
  <div class="about-media" role="img" aria-label="Counsellor talking with a young man in a hoodie, video">
    <span class="play" style="left:118px;top:84px"><svg width="34" height="34" viewBox="0 0 34 34"><path d="M13 10 L24 17 L13 24Z" fill="#2f4a8f"/></svg></span>
  </div>
</section>

<footer class="site-footer">
  <div class="footer-brand"><span class="brand-dot"></span><span class="brand-name">Kolrev AB</span></div>
  <div class="footer-col" style="left:174px">
    <h4>Contact</h4>
    <ul class="contact-list">
      <li><svg width="18" height="22" viewBox="0 0 18 22"><path d="M9 21 Q1 11 1 8 A8 8 0 0 1 17 8 Q17 11 9 21Z" fill="none" stroke="#8cb83a" stroke-width="1.5"/><circle cx="9" cy="8" r="3" fill="none" stroke="#8cb83a" stroke-width="1.5"/></svg><span>Kolrev Sverige AB<br>Lindåsvägen 1145, 264 90 Norrby</span></li>
      <li><svg width="20" height="20" viewBox="0 0 34 34"><path d="M8 4 L13 10 L10 14 Q13 21 20 24 L24 21 L30 26 L26 31 Q12 30 3 10 Z" fill="none" stroke="#8cb83a" stroke-width="2.4"/></svg><span>010-4407215</span></li>
      <li><svg width="20" height="16" viewBox="0 0 20 16"><rect x="1" y="1" width="18" height="14" fill="none" stroke="#8cb83a" stroke-width="1.5"/><path d="M1 1 L10 9 L19 1 M1 15 L8 8 M19 15 L12 8" fill="none" stroke="#8cb83a" stroke-width="1.5"/></svg><span>info@kolrev.se</span></li>
    </ul>
    <div class="org">Org nr 556412-3390</div>
    <a class="btn" href="#">Have a Query</a>
  </div>
  <div class="footer-col" style="left:466px">
    <h4>kolrev.se</h4>
    <ul class="links">
      <li>About us</li><li>Team</li><li>Quality Work</li><li>Values base</li><li>Ekbacken HVB</li><li>Treament</li><li>Career</li>
    </ul>
  </div>
  <div class="footer-col newsletter" style="left:758px">
    <h4>Newsletter</h4>
    <p>Subscribe to our Newsletter<br>for latest updates</p>
    <div class="signup"><span>Your email |</span><b>Submit</b></div>
    <h4 style="margin-top:30px">Socials</h4>
    <div class="socials">
      <div class="social" role="img" aria-label="Social profile photo, fishing trip" style="background:linear-gradient(135deg,#2f6fa6,#6b5a4c)"><i style="background:var(--blue)"></i></div>
      <div class="social" role="img" aria-label="Social profile photo, living room" style="background:linear-gradient(135deg,#d8d4ce,#5a4e46)"><i style="background:var(--blue)"></i></div>
      <div class="social" role="img" aria-label="Social profile photo, boat outing" style="background:linear-gradient(135deg,#4f6e3a,#2e4d6e)"><i style="background:var(--red)"></i></div>
    </div>
  </div>
</footer>
<div class="copyright">Copyright kolrev.se | 2018</div>

</body>
</html>
```